Flyer needed to promote gutter clearance service for established gardening company

We need a bright and engaging flyer to be designed to advertise our gutter clearance service.
Whilst we are a gardening company that normally does more horticultural work, during the winter we offer other services such as gutter clearance where we remove the debris from gutters and thereby reducing the risk of clogs, leakage, breakage and potential structural damage to the property.

Full details of our service, together with our overall brand and colours can be seen on www.marlowtreecare.co.uk/gutters.

We would like you to use the page on the website as a basis to create the flyer and so please feel free to use as much or as little of the wording contained within the webpage on the flyer drawing particular attention to "Prices starting at just £60 for an average 3 bed house". I will upload pictures but please feel free to use other graphics and fonts to make it stand out.

The contact details which should be included within the flyer are as follows:

Marlow Treecare Services Ltd
Orbit Trading Centre
Fairbrook Vale Ind Estate
Swindon
SN4 7HW

Tel: 01793 418302
www.marlowtreecare.co.uk
dean@marlowtreecare.co.uk

The flyers will eventually be printed out in A5 (210mm x 148mm) using Printelle and so needs to be in that size and suitable file for upload.

I have only put this as a 2 day project as its really urgent and I'm hoping we get some great designs in that time.

Target Market(s)

Homeowners between 25 - 65+

Industry/Entity Type

Home Improvement

Font styles to use
Serif
Sans Serif
Decorative
Script

Colors
6b449b
9bcb3c

Requirements
Must have
• Our colours are purple and green as seen on our website www.marlowtreecare.co.uk/gutters. Please use those colours.
• The flyer should draw attention to the following facts:
• We are Marlow Treecare Services Ltd (see attached logo)
• We are offering a Gutter Clearance Service in Swindon
• Prices start at just £60 for the average 3 bed house.
• We are fully insured.
• Our contact details must be included (as in the product description above)
• I have attached pictures but feel free to add other graphics or use fonts to make the flyer more engaging and interesting.
• Additional wording may be taken from the website at the address shown above. You can use as much or as little wording as you like just as long as the message gets across and the flyer contains our contact information and logo and the details shown above.
Nice to have
• I would like a bright and modern design which isn't too busy or cluttered. It should be something that is quick and easy to read.
Should not have
• I don't want it to look too busy or crowded with small type which people just won't read. Whilst I've said you can take whatever wording you want from our website, I'd suggest you don't take it all or too much. I want the main message (as detailed above in 'must haves') to stand out rather than have it contained deep within lots of small type face.

```html
<!DOCTYPE html>
<html lang="en">
<head>
<meta charset="utf-8">
<title>Gutter Clearance Flyer</title>
<link rel="stylesheet" href="https://fonts.googleapis.com/css2?family=Antonio:wght@400;700&display=swap">
<style>
  :root {
    --purple: #6b449b;
    --green: #9bcb3c;
    --lime-light: #e4ea9a;
    --lime-mid: #d2dd6a;
    --peach: #f4d7b4;
    --peach-light: #f8e6cf;
    --band-white: #f7f7f5;
    --stage: #e9e9e9;
    --ink: #3a3a1e;
    --stone: #8f8c86;
    --debris: #8a7a45;
    --clean: #a9a49a;
    --lawn: #6aa13a;
  }
  * { margin: 0; padding: 0; box-sizing: border-box; }
  html, body { width: 1200px; height: 700px; overflow: hidden; background: var(--stage); }
  .flyer {
    position: absolute; left: 150px; top: 0; width: 1050px; height: 700px;
    font-family: "Antonio", "Arial Narrow", sans-serif;
    overflow: hidden; background: var(--band-white);
  }
  .intro {
    position: absolute; left: 0; top: 0; width: 770px; height: 125px;
    background: linear-gradient(120deg, var(--lime-light), var(--lime-mid) 55%, #e9ee9f);
  }
  .intro-text {
    position: absolute; font-size: 20px; font-weight: 700; text-transform: uppercase;
    color: var(--ink); line-height: 1.2;
  }
  .intro-text.left { left: 58px; top: 4px; }
  .intro-text.right { right: 60px; top: 4px; text-align: right; }
  .photo-roof {
    position: absolute; left: 770px; top: 0; width: 280px; height: 125px;
    background: linear-gradient(160deg, #6f6c66, var(--stone) 60%, #5e6a48);
  }
  .price-band {
    position: absolute; left: 0; top: 125px; width: 1050px; height: 114px;
    background: var(--purple);
  }
  .price-band p {
    position: absolute; left: 0; top: 10px; width: 1050px; text-align: center;
    color: #fff; font-size: 42px; line-height: 46px; font-weight: 400; letter-spacing: 0.5px;
  }
  .peach {
    position: absolute; left: 0; top: 239px; width: 1050px; height: 51px;
    background: linear-gradient(90deg, var(--peach), var(--peach-light) 60%, #f1e0a8);
  }
  .compare-band {
    position: absolute; left: 0; top: 290px; width: 1050px; height: 128px;
    background: var(--band-white);
  }
  .label {
    position: absolute; font-size: 48px; font-weight: 400; line-height: 1.15;
    letter-spacing: 16px; text-transform: uppercase;
  }
  .label.before { left: 18px; top: 2px; color: var(--green); }
  .label.after { right: 0; top: 40px; color: var(--purple); }
  .photo { position: absolute; }
  .photo.before { left: 15px; top: 370px; width: 455px; height: 330px;
    background: linear-gradient(90deg, var(--stone) 0 90px, var(--debris) 90px 300px, #d8d8d2 300px 340px, var(--lawn) 340px); }
  .photo.after { left: 478px; top: 418px; width: 572px; height: 282px;
    background: linear-gradient(90deg, #6e5a4c 0 150px, var(--clean) 150px 440px, #dedede 440px 470px, var(--lawn) 470px); }
</style>
</head>
<body>
  <main class="flyer">
    <section class="intro">
      <p class="intro-text left">Save climbing ladders<br>and getting injured</p>
      <p class="intro-text right">No need to risk getting dirty or<br>hurting yourself.</p>
    </section>
    <div class="photo-roof" role="img" aria-label="Photo of a roof edge and gutter"></div>
    <section class="price-band">
      <p>with prices starting at just £60 to clear the<br>gutters of an average 3 bed house!</p>
    </section>
    <div class="peach"></div>
    <section class="compare-band">
      <h2 class="label before">Before</h2>
      <h2 class="label after">After</h2>
    </section>
    <div class="photo before" role="img" aria-label="Photo of a gutter clogged with leaves before clearance"></div>
    <div class="photo after" role="img" aria-label="Photo of the same gutter clean after clearance"></div>
  </main>
</body>
</html>
```